Fancy flyer to entice High School Students

http://quillmarsh.com needs a marketing slick/flyer to pass out. The marketing text is below(feel free to place where you think appropriate).

* 8th grade to 12th grade (or 8th graders to 12th graders)
* Land a real job internship(instead of Grubbins)
* 100's of internships available
* Learn how to start your own business out of High School making way more than minimum wage
* In college when interviewing for an internship don't be the guy that answers "no, sorry, this would be my first internship" putting you at a huge disadvantage"
* Fill in the Contact Us form at http://quillmarsh.com at the bottom left corner to find out more information

We will be evaluating design with this blog post in mind....
http://trovelinkdigest.com/color-influence-buyers/

We like attention grabbing contact us type stuff and calls to action. If you feel it is appropriate to change the marketing text to make your flyer stand out, please feel free. I am not the best at marketing and am the first to admit it.
Updates

A simple 8.5 x 11 flyer would be great.

Target Market(s)

High School students, male and female with high grade point averages(smart students). For the top 20% of their class.

Industry/Entity Type

Marketing

Requirements
Must have
• good call to action

```html
<!DOCTYPE html>
<html lang="en">
<head>
<meta charset="utf-8">
<title>Quillmarsh Software – Student Internships Flyer</title>
<link rel="stylesheet" href="https://fonts.googleapis.com/css2?family=Didact+Gothic&display=swap">
<style>
  :root {
    --navy: #0b0b47;
    --navy-line: #14145a;
    --panel-top: #c3d2de;
    --panel-bottom: #93aabd;
    --tab-line: #9fb3c6;
    --ink: #0d0d4c;
    --white: #ffffff;
    --logo-bg: rgba(255,255,255,0.82);
    --logo-ink: #2a2a2a;
  }
  * { margin: 0; padding: 0; box-sizing: border-box; }
  html, body { width: 927px; height: 1200px; overflow: hidden; background: var(--navy); }
  .flyer {
    position: relative;
    width: 927px; height: 1200px;
    background: var(--navy);
    font-family: "Didact Gothic", "Century Gothic", sans-serif;
    overflow: hidden;
  }
  .hero-photo {
    position: absolute; left: 0; top: 14px; width: 927px; height: 636px;
    background:
      radial-gradient(ellipse at 78% 30%, #e8cdbb 0%, rgba(232,205,187,0) 22%),
      radial-gradient(ellipse at 80% 75%, #b9d3ea 0%, rgba(185,211,234,0) 40%),
      linear-gradient(180deg, #3d524b 0%, #4a5e57 45%, #c9ced3 70%, #e9ecef 100%);
  }
  .brand {
    position: absolute; left: 0; top: 26px; width: 290px; height: 58px;
    background: var(--logo-bg);
    display: flex; align-items: center; gap: 10px; padding-left: 18px;
  }
  .brand-dot { width: 14px; height: 14px; border-radius: 50%; background: var(--logo-ink); }
  .brand-name { font-size: 25px; color: var(--logo-ink); }
  .side-tab {
    position: absolute; width: 40px; top: 668px; height: 378px;
    background: var(--navy);
  }
  .side-tab.left { left: 0; }
  .side-tab.right { right: 0; }
  .side-tab span {
    position: absolute; left: 0; right: 0; height: 2px; background: var(--tab-line);
  }
  .info-panel {
    position: absolute; left: 40px; top: 668px; width: 847px; height: 378px;
    background: linear-gradient(180deg, var(--panel-top), var(--panel-bottom));
    color: var(--ink); text-align: center; font-size: 28px; line-height: 37px;
  }
  .point { position: absolute; left: 0; right: 0; }
  .divider {
    position: absolute; left: 52px; right: 52px; height: 4px; background: var(--navy-line);
  }
  .cta {
    position: absolute; left: 0; right: 0; top: 1068px;
    color: var(--white); text-align: center; font-size: 28px; line-height: 38px;
  }
</style>
</head>
<body>
<div class="flyer">
  <div class="hero-photo" role="img" aria-label="Photo of a smiling student at a classroom desk, with classmates and a teacher at a chalkboard behind him"></div>

  <div class="brand">
    <span class="brand-dot"></span>
    <span class="brand-name">Quillmarsh Software</span>
  </div>

  <div class="side-tab left">
    <span style="top:48px"></span><span style="top:100px"></span>
    <span style="top:152px"></span><span style="top:240px"></span>
  </div>
  <div class="side-tab right">
    <span style="top:48px"></span><span style="top:100px"></span>
    <span style="top:152px"></span><span style="top:240px"></span>
  </div>

  <div class="info-panel">
    <p class="point" style="top:6px">8th graders to 12th graders</p>
    <div class="divider" style="top:48px"></div>
    <p class="point" style="top:58px">Land a real job internship (instead of Grubbins)</p>
    <div class="divider" style="top:100px"></div>
    <p class="point" style="top:110px">100's of internships available</p>
    <div class="divider" style="top:152px"></div>
    <p class="point" style="top:160px">Learn how to start your own business out of<br>High School making way more than minimum wage</p>
    <div class="divider" style="top:238px"></div>
    <p class="point" style="top:255px">In college when interviewing for an internship don't be<br>the guy that answers "no, sorry, this would be my first<br>internship" putting you at a huge disadvantage"</p>
  </div>

  <p class="cta">Fill in the Contact Us form at<br>http://quillmarsh.com<br>at the bottom left corner to find out more information</p>
</div>
</body>
</html>
```